Morvek Menu

Hi there,
My restaurant called "Morvek" means Spice in hebrew.
We are middle eastern restaurant that specialist in dips,salads and hot bread baked on the spot and charcoal grilled meat skewers
The restaurant is pretty casual and the atmosphere is nice and customers feels like home.
on www.morvek.com.au you can see photos of the restaurant and the food.
ill add up the menus that i would like to be design please and the logo that is on the front of the shop is been add up
thank you

Target Market(s)

The regulars of the restaurant is jewish/israelis

Industry/Entity Type

Restaurant

```html
<!DOCTYPE html>
<html lang="en">
<head>
<meta charset="utf-8">
<title>Morvek – Take Away Menu</title>
<link rel="stylesheet" href="https://fonts.googleapis.com/css2?family=Cinzel:wght@400;700&family=Marcellus&display=swap">
<style>
  :root {
    --bg-center: #8a0f12;
    --bg-mid: #5a0608;
    --bg-edge: #1e0203;
    --gold: #e3b35a;
    --gold-soft: #b27a3a;
    --gold-line: #d9a854;
    --cream: #f4e9d2;
    --band: #2a0506;
  }
  * { margin: 0; padding: 0; box-sizing: border-box; }
  html, body { width: 849px; height: 1200px; overflow: hidden; background: var(--bg-edge); }
  .menu {
    position: relative;
    width: 849px; height: 1200px;
    background: radial-gradient(ellipse 70% 60% at 50% 45%, var(--bg-center) 0%, var(--bg-mid) 50%, var(--bg-edge) 100%);
    font-family: "Cinzel", "Times New Roman", serif;
    color: var(--gold);
    overflow: hidden;
  }
  .frame { position: absolute; inset: 0; }
  .ornament { position: absolute; background: radial-gradient(ellipse at center, #e8bf6a 0%, #a8762f 60%, rgba(168,118,47,0) 100%); }
  .ornament--top { left: 370px; top: 8px; width: 110px; height: 38px; }
  .ornament--bottom { left: 370px; top: 1150px; width: 110px; height: 38px; }
  .ornament--left { left: 10px; top: 522px; width: 40px; height: 145px; }
  .ornament--right { left: 798px; top: 534px; width: 40px; height: 145px; }

  .brand {
    position: absolute; left: 0; width: 849px; top: 78px;
    text-align: center; font-size: 54px; font-weight: 400; color: var(--cream);
    letter-spacing: 1px;
  }
  .banner {
    position: absolute; left: 313px; top: 222px; width: 220px; height: 96px;
    background: linear-gradient(to bottom, rgba(20,2,3,0.85), rgba(60,6,8,0.6));
  }
  .banner__text {
    position: absolute; left: 0; width: 849px; top: 250px; text-align: center;
    font-family: "Marcellus", "Times New Roman", serif; font-size: 25px; color: #eccf97; letter-spacing: 0.5px;
  }
  .contact {
    position: absolute; left: 0; width: 849px; top: 360px; text-align: center;
    font-size: 15px; line-height: 20px; color: var(--gold-soft);
  }
  .section { position: absolute; left: 0; width: 849px; text-align: center; font-weight: 700; }
  .section__title { font-size: 23px; line-height: 28px; text-decoration: underline; text-underline-offset: 3px; }
  .section__note { font-size: 16px; line-height: 24px; }
  .section__list { list-style: none; font-size: 17px; line-height: 24px; }
  .section--dips { top: 478px; }
  .section--dips .section__list { margin-top: 26px; }
  .section--wraps { top: 816px; }
</style>
</head>
<body>
<main class="menu">
  <svg class="frame" width="849" height="1200" viewBox="0 0 849 1200" aria-hidden="true">
    <g stroke="var(--gold-line)" fill="none" stroke-width="1.2">
      <line x1="18" y1="0" x2="18" y2="1200"/>
      <line x1="28" y1="0" x2="28" y2="1200"/>
      <line x1="821" y1="0" x2="821" y2="1200"/>
      <line x1="831" y1="0" x2="831" y2="1200"/>
      <line x1="0" y1="14" x2="849" y2="14"/>
      <line x1="0" y1="26" x2="849" y2="26"/>
      <line x1="0" y1="1174" x2="849" y2="1174"/>
      <line x1="0" y1="1186" x2="849" y2="1186"/>
      <path d="M313 318 Q423 300 533 318" stroke-width="1.5"/>
    </g>
  </svg>
  <div class="ornament ornament--top" role="img" aria-label="Gold scroll ornament"></div>
  <div class="ornament ornament--bottom" role="img" aria-label="Gold scroll ornament"></div>
  <div class="ornament ornament--left" role="img" aria-label="Gold scroll ornament"></div>
  <div class="ornament ornament--right" role="img" aria-label="Gold scroll ornament"></div>

  <h1 class="brand">Morvek</h1>
  <div class="banner"></div>
  <p class="banner__text">TAKE AWAY MENU</p>

  <p class="contact">412 Larkmoor Road, Ashbridge South<br>Tel.&nbsp; 9031 4872</p>

  <section class="section section--dips">
    <h2 class="section__title">Salads &amp; Dips</h2>
    <p class="section__note">Small $5.50 / Large $10.00 / Jumbo $16.00</p>
    <ul class="section__list">
      <li>Baba Ganoush (GF)</li>
      <li>Turkish (GF)</li>
      <li>Chatzilim (Fried Eggplant) (GF)</li>
      <li>Corn Salad (GF)</li>
      <li>Mixed Pickles (GF)</li>
      <li>Moroccan Carrot (GF)</li>
      <li>Roasted Beetroot (GF)</li>
      <li>Hummus (GF)</li>
      <li>Tahini (GF)</li>
      <li>White cabbage (GF)</li>
    </ul>
  </section>

  <section class="section section--wraps">
    <h2 class="section__title">Laffa Wraps</h2>
    <p class="section__note">Served with Hummus, Tahini, Israeli Salad and Pickles<br>(One large skewer per serve)</p>
    <ul class="section__list">
      <li>Falafel $12.00</li>
      <li>Chicken Shashlik $14.00</li>
      <li>Lamb Shashlik $15.00</li>
      <li>Kofta $13.00</li>
      <li>Liver Shashlik $13.50</li>
      <li>Schnitzel $13.00</li>
    </ul>
  </section>
</main>
</body>
</html>
```